Tolvane's 50th Anniversary Gala

Need a cool invitation to be printed on #120 paper for a nonprofit gala fundraiser. Verbiage for invitation is below. Event logo is attached. Could potentially use black and gold but NOT a requirement. Want it to be FUN and DIFFERENT.

Colors
0054AA
0677BA
7BADD7
CADEEF
E8F1F8

```html
<!DOCTYPE html>
<html lang="en">
<head>
<meta charset="utf-8">
<title>Tolvane's 50th Anniversary Gala – Invitation</title>
<link rel="stylesheet" href="https://fonts.googleapis.com/css2?family=Great+Vibes&family=Playfair+Display:wght@400&family=Source+Sans+3:ital,wght@1,300&display=swap">
<style>
  :root {
    --page: #ffffff;
    --navy: #0d0f40;
    --gold-frame: #d6b257;
    --gold-text: #d8b464;
    --gold-light: #f4e4a2;
  }
  html, body {
    margin: 0;
    width: 1200px;
    height: 1000px;
    overflow: hidden;
    background: var(--page);
  }
  .invitation {
    position: absolute;
    left: 345px;
    top: 135px;
    width: 510px;
    height: 730px;
    background: var(--navy);
  }
  .invitation__frame {
    position: absolute;
    inset: 11px;
    border: 11px solid var(--gold-frame);
  }
  .line {
    position: absolute;
    left: 0;
    right: 0;
    margin: 0;
    text-align: center;
    white-space: nowrap;
  }
  .script {
    font-family: "Great Vibes", cursive;
    color: var(--gold-light);
    font-weight: 400;
  }
  .serif {
    font-family: "Playfair Display", serif;
    color: var(--gold-text);
    font-size: 22px;
    line-height: 1;
  }
  .welcome { top: 52px; font-size: 36px; }
  .event-mark {
    top: 150px;
    font-family: "Playfair Display", serif;
    font-size: 64px;
    line-height: 1;
    color: var(--gold-light);
    letter-spacing: 1px;
  }
  .event-title { top: 270px; font-size: 58px; }
  .date { top: 366px; }
  .time { top: 401px; }
  .venue { top: 465px; }
  .address { top: 499px; }
  .menu { top: 555px; font-size: 39px; }
  .divider {
    position: absolute;
    top: 624px;
    left: 50%;
    transform: translateX(-50%);
  }
  .footnotes {
    position: absolute;
    top: 679px;
    left: 0;
    right: 0;
    display: flex;
    justify-content: center;
    gap: 25px;
    font-family: "Source Sans 3", sans-serif;
    font-style: italic;
    font-weight: 300;
    font-size: 14px;
    color: var(--gold-text);
    padding-left: 16px;
  }
</style>
</head>
<body>
  <main class="invitation">
    <div class="invitation__frame"></div>

    <p class="line script welcome">Join us for a memorable night!</p>

    <p class="line event-mark">Tolvane</p>

    <h1 class="line script event-title">Gala Celebration</h1>

    <p class="line serif date">Friday, November 8th</p>
    <p class="line serif time">6:30 – 10 p.m</p>

    <p class="line serif venue">The Marlowe</p>
    <p class="line serif address">2416 North Halden Street</p>

    <p class="line script menu">Hors d’oeuvres and Cocktails</p>

    <svg class="divider" width="56" height="8" viewBox="0 0 56 8" aria-hidden="true">
      <g fill="var(--gold-text)">
        <circle cx="4" cy="4" r="2.2"/>
        <circle cx="16" cy="4" r="2.2"/>
        <circle cx="28" cy="4" r="2.2"/>
        <circle cx="40" cy="4" r="2.2"/>
        <circle cx="52" cy="4" r="2.2"/>
      </g>
    </svg>

    <div class="footnotes">
      <span>Semi-formal</span>
      <span>Ticket information on reverse</span>
    </div>
  </main>
</body>
</html>
```